TEK Logistics - Banner 2.5' x 8' for 20+ locations

Need a banner designed that will pop. This banner will be displayed at over 20 of our transportation facilities. Goal is for the banner to grab the attention of employees, contractors and clients and help reinforce our mission and core values. Designed needs to include TEK Logo, our core values and mission statement. Red and Black are the main company colors and we need to stay within that theme and color pallet. Attached is a previous version that was too basic and boring. Willing to consider a design that excludes the mission statement.

Gathering more feedback

```html
<!DOCTYPE html>
<html lang="en">
<head>
<meta charset="utf-8">
<title>TEK Logistics Banner</title>
<link rel="stylesheet" href="https://fonts.googleapis.com/css2?family=Exo+2:wght@400;500;700&family=Raleway:wght@400;500;700&display=swap">
<style>
  :root {
    --brand-red: #d71f27;
    --brand-black: #1b1716;
    --paper: #ffffff;
    --ink: #1e1b1a;
    --backdrop: #5f5f5f;
  }
  * { margin: 0; padding: 0; box-sizing: border-box; }
  html, body { width: 1110px; height: 1200px; overflow: hidden; }
  body { background: var(--backdrop); position: relative; }

  .banner {
    position: absolute;
    left: 40px; top: 439px;
    width: 1030px; height: 322px;
    background: var(--paper);
    overflow: hidden;
    box-shadow: 0 14px 22px rgba(0,0,0,0.35);
  }
  .banner-shapes, .banner-photo { position: absolute; left: 0; top: 0; }

  .logo-lockup {
    position: absolute;
    left: 254px; top: 103px;
    width: 174px; height: 174px;
    display: flex; align-items: center; justify-content: center;
  }
  .logo-name {
    font-family: "Exo 2", sans-serif;
    font-weight: 700;
    font-size: 24px;
    color: var(--brand-red);
  }

  .mission {
    position: absolute;
    left: 453px; top: 18px;
    width: 570px;
    font-family: "Exo 2", sans-serif;
    font-weight: 500;
    font-size: 23.5px;
    line-height: 30.5px;
    color: var(--ink);
  }
  .mission .highlight { color: var(--brand-red); }

  .rule {
    position: absolute;
    left: 453px; top: 125px;
    width: 66px; height: 3px;
    background: var(--brand-red);
  }

  .values-title {
    position: absolute;
    left: 453px; top: 141px;
    font-family: "Raleway", sans-serif;
    font-weight: 700;
    font-size: 19px;
    color: var(--ink);
  }
  .values-list {
    position: absolute;
    top: 172px;
    list-style: none;
    font-family: "Raleway", sans-serif;
    font-weight: 500;
    font-size: 16px;
    line-height: 17.6px;
    color: var(--ink);
  }
  .values-list.col-a { left: 453px; }
  .values-list.col-b { left: 775px; }
  .values-list li { position: relative; padding-left: 12px; white-space: nowrap; }
  .values-list li::before {
    content: ""; position: absolute; left: 0; top: 6px;
    width: 7px; height: 7px; border-radius: 50%;
    background: var(--brand-red);
  }

  .contact-phone {
    position: absolute;
    left: 424px; top: 268px;
    display: flex; align-items: center; gap: 4px;
    font-family: "Exo 2", sans-serif;
    font-weight: 500;
    font-size: 31px;
    color: var(--paper);
    line-height: 38px;
  }
  .contact-web {
    position: absolute;
    left: 711px; top: 263px;
    width: 299px; height: 48px;
    background: var(--paper);
    display: flex; align-items: center; justify-content: center;
    font-family: "Exo 2", sans-serif;
    font-weight: 400;
    font-size: 27px;
    color: var(--ink);
  }
  .contact-web .domain { color: var(--brand-red); }
</style>
</head>
<body>
  <section class="banner">
    <svg class="banner-shapes" width="1030" height="322" viewBox="0 0 1030 322" aria-hidden="true">
      <path class="contact-band" d="M390,250 H1030 V322 H340 Z" fill="var(--brand-black)"/>
    </svg>

    <svg class="banner-photo" width="1030" height="322" viewBox="0 0 1030 322" role="img" aria-label="Photo of a box truck driving down a highway at sunset">
      <defs>
        <linearGradient id="photoTone" x1="0" y1="0" x2="0.4" y2="1">
          <stop offset="0" stop-color="#6e5e7c"/>
          <stop offset="0.35" stop-color="#e9a35a"/>
          <stop offset="0.6" stop-color="#f1c48a"/>
          <stop offset="1" stop-color="#b48467"/>
        </linearGradient>
        <radialGradient id="sunGlow" cx="0.15" cy="0.55" r="0.45">
          <stop offset="0" stop-color="#fff3cf" stop-opacity="0.95"/>
          <stop offset="1" stop-color="#f5b55a" stop-opacity="0"/>
        </radialGradient>
      </defs>
      <path d="M0,0 H290 C370,8 428,90 432,175 C434,245 398,298 340,322 H0 Z" fill="url(#photoTone)"/>
      <path d="M0,0 H290 C370,8 428,90 432,175 C434,245 398,298 340,322 H0 Z" fill="url(#sunGlow)"/>
      <path d="M285,0 C370,6 432,88 434,172" fill="none" stroke="var(--brand-red)" stroke-width="10"/>
      <path d="M110,110 C140,55 200,40 250,48" fill="none" stroke="var(--paper)" stroke-width="4"/>
      <path d="M140,280 C180,310 240,322 290,322" fill="none" stroke="var(--brand-red)" stroke-width="5"/>
      <circle cx="341" cy="190" r="87" fill="var(--paper)"/>
    </svg>

    <div class="logo-lockup">
      <span class="logo-name">TEK Logistics</span>
    </div>

    <p class="mission">Provide the <span class="highlight">best customer experience</span> while creating an environment of growth and opportunity for our customers, employees, and service providers.</p>
    <div class="rule"></div>

    <h2 class="values-title">Core Values:</h2>
    <ul class="values-list col-a">
      <li>Do the right things for the right reasons</li>
      <li>Pursue growth and development</li>
      <li>Build a positive team atmosphere</li>
    </ul>
    <ul class="values-list col-b">
      <li>Deliver WOW through service</li>
      <li>Do everything Safely</li>
      <li>Have Fun</li>
    </ul>

    <div class="contact-phone">
      <svg width="30" height="30" viewBox="0 0 30 30" aria-hidden="true">
        <path d="M6,4 L11,3 L14,10 L11,12 C12,16 14,18 18,19 L20,16 L27,19 L26,24 C24,27 20,27 16,25 C10,22 7,18 5,13 C4,9 4,6 6,4 Z" fill="var(--brand-red)"/>
        <path d="M17,7 A7,7 0 0 1 23,13" fill="none" stroke="var(--brand-red)" stroke-width="2"/>
        <path d="M18,2 A11,11 0 0 1 28,12" fill="none" stroke="var(--brand-red)" stroke-width="2"/>
      </svg>
      <span>(866) 555--0142</span>
    </div>

    <div class="contact-web">www.<span class="domain">teklogistics</span>.com</div>
  </section>
</body>
</html>
```